fernbolt website

commerce website to sell cookeries, brackets, mailboxes and to show off homes built. Modern Steel in design see kelvo rides web page to be like: https://www.kelvorides.com/en/ sorry its blue mantis hosting word press divi

must be able to add products to page

Target Market(s)

mainly western states of U.S.

Industry/Entity Type

Building Product

Coding

Coded - Design and coding required

Number of Pages Required

3 page

Font styles to use
Sans Serif

Colors

Designer to choose colors to be used in the design.

Requirements
Must have
• customers to be able to order products from page
• blue mantis hosting word press divi

```html
<!DOCTYPE html>
<html lang="en">
<head>
<meta charset="utf-8">
<title>Fernbolt — Modern Steel</title>
<link rel="stylesheet" href="https://fonts.googleapis.com/css2?family=Fira+Sans:wght@300;400;500;600;700;800&display=swap">
<style>
  :root{
    --navy:#44608e;
    --navy-deep:#1e2c4a;
    --navy-mid:#2f4670;
    --footer:#22304d;
    --orange:#ff7d0a;
    --white:#ffffff;
    --ink:#1c1c1c;
  }
  *{box-sizing:border-box;margin:0;padding:0}
  html,body{width:943px;height:1200px;overflow:hidden;background:var(--white)}
  body{position:relative;font-family:"Fira Sans",sans-serif;color:var(--white)}
  a{color:inherit;text-decoration:none}

  /* header */
  .topbar{position:absolute;left:0;top:0;width:943px;height:57px;background:var(--navy);z-index:3}
  .brand{position:absolute;left:124px;top:18px;display:flex;align-items:center;gap:6px;font-weight:600;font-size:17px;letter-spacing:1px;color:var(--white)}
  .brand .mark{width:12px;height:12px;background:var(--white)}
  .search{position:absolute;left:300px;top:13px;width:283px;height:32px;background:var(--white);border-radius:2px;display:flex;align-items:center}
  .search span{font-size:10px;color:#8a8f98;padding-left:11px;letter-spacing:.6px;flex:1}
  .search .divider{width:1px;height:18px;background:#9aa3b3}
  .search svg{margin:0 11px 0 9px}
  .account{position:absolute;left:631px;top:20px;display:flex;gap:12px;font-size:11px;font-weight:500;align-items:center}
  .account .item{display:flex;align-items:center;gap:4px}
  .account .cart{margin-left:10px}
  .cart-count{position:absolute;font-size:8px;left:150px;top:-5px}

  .mainnav{position:absolute;left:124px;top:57px;width:819px;height:33px;background:var(--white);color:var(--ink);font-size:11px;font-weight:500;z-index:3}
  .mainnav a,.mainnav .sep{position:absolute;top:10px}
  .lang{position:absolute;left:559px;top:11px;display:flex;gap:4px;align-items:center}
  .navrule{position:absolute;left:609px;top:8px;width:1px;height:17px;background:#d7dbe2}
  .mainnav .social-sm{position:absolute;top:5px;width:22px;height:22px;border:1.3px solid var(--navy);border-radius:50%;color:var(--navy);font-size:7px;font-weight:600;display:flex;align-items:center;justify-content:center}

  /* hero */
  .hero{position:absolute;left:0;top:57px;width:943px;height:384px;background:linear-gradient(120deg,#1f3158 0%,var(--navy-deep) 55%,#1b2945 100%);overflow:hidden;z-index:1}
  .hero svg.shapes{position:absolute;left:0;top:0}
  .hero-title{position:absolute;left:124px;top:86px;font-weight:700;font-size:48px;line-height:50px;letter-spacing:2px}
  .hero-sub{position:absolute;left:125px;top:196px;font-size:17px;line-height:21px;font-weight:400}
  .hero-text{position:absolute;left:124px;top:247px;font-size:11px;line-height:18px;font-weight:300;width:205px}
  .btn{position:absolute;left:124px;top:294px;width:106px;height:33px;background:var(--white);color:var(--navy-deep);font-weight:700;font-size:10px;display:flex;align-items:center;justify-content:center;border-radius:2px}
  .slider{position:absolute;left:359px;top:352px;width:224px;height:32px;background:var(--orange)}
  .slider .dot{position:absolute;top:11px;width:8px;height:8px;border-radius:50%;background:var(--white)}
  .slider .dot.active{background:var(--navy-mid);border:2px solid var(--white)}
  .slider .line{position:absolute;left:140px;top:15px;width:59px;height:1px;background:var(--white)}

  /* categories */
  .card{position:absolute;top:465px;width:224px;height:222px;background:var(--white);box-shadow:0 1px 4px rgba(0,0,0,.18);padding:2px}
  .card .photo{width:220px;height:187px}
  .card .label{height:33px;background:var(--navy);display:flex;align-items:center;justify-content:space-between;padding:0 11px;font-weight:800;font-size:16px;letter-spacing:.2px}

  /* footer */
  .footer{position:absolute;left:0;top:745px;width:943px;height:455px;background:linear-gradient(135deg,#243354 0%,var(--footer) 50%,#1f2b45 100%)}
  .f-brand{position:absolute;left:124px;top:120px;display:flex;align-items:center;gap:8px;font-weight:600;font-size:24px;letter-spacing:1.5px}
  .f-brand .mark{width:16px;height:16px;background:var(--white)}
  .contact{position:absolute;left:124px;font-size:11px;line-height:18px;letter-spacing:.2px}
  .contact svg{position:absolute;left:8px;top:2px}
  .contact p{padding-left:29px}
  .col{position:absolute;top:127px;padding-left:30px;border-left:1px solid #3d5278;height:159px}
  .col h3{font-size:16px;font-weight:600;letter-spacing:.3px;margin-left:-1px}
  .col ul{list-style:none;margin-top:21px;font-size:11px;letter-spacing:.2px}
  .col li{height:26px}
  .f-rule{position:absolute;left:124px;top:335px;width:695px;height:1px;background:#6b7a96}
  .copy{position:absolute;left:124px;top:369px;font-size:10px}
  .social-lg{position:absolute;top:358px;width:34px;height:34px;border:1.3px solid var(--white);border-radius:50%;font-size:9px;font-weight:500;display:flex;align-items:center;justify-content:center}
  .pay{position:absolute;top:364px;display:flex;align-items:center;justify-content:center;height:21px;font-size:8px;font-weight:600;border-radius:2px}
  .pay.first{font-size:17px;font-weight:700;color:var(--white)}
  .pay.card-chip{background:var(--white);color:var(--navy-deep);width:31px}
</style>
</head>
<body>

<header class="topbar">
  <div class="brand"><span class="mark"></span>FERNBOLT</div>
  <div class="search">
    <span>Enter your key words...</span>
    <i class="divider"></i>
    <svg width="13" height="13" viewBox="0 0 13 13"><circle cx="5.5" cy="5.5" r="4.3" fill="none" stroke="#44608e" stroke-width="1.8"/><line x1="8.7" y1="8.7" x2="12" y2="12" stroke="#44608e" stroke-width="2"/></svg>
  </div>
  <nav class="account">
    <a class="item" href="#"><svg width="13" height="10" viewBox="0 0 13 10"><rect x="1" y="3" width="9" height="6" fill="none" stroke="#fff" stroke-width="1.2"/><rect x="4" y="1" width="8" height="5" fill="#fff"/></svg>REGISTER</a>
    <a class="item" href="#"><svg width="9" height="10" viewBox="0 0 9 10"><circle cx="4.5" cy="3" r="2.2" fill="#fff"/><path d="M0.5 10 Q4.5 4.5 8.5 10Z" fill="#fff"/></svg>LOG IN</a>
    <a class="item cart" href="#"><svg width="20" height="18" viewBox="0 0 20 18"><path d="M1 2 H4 L6 12 H16 L18 5" fill="none" stroke="#fff" stroke-width="1.4"/><circle cx="7.5" cy="15.5" r="1.6" fill="none" stroke="#fff" stroke-width="1.2"/><circle cx="14.5" cy="15.5" r="1.6" fill="none" stroke="#fff" stroke-width="1.2"/></svg>Cart</a>
    <span class="cart-count">0</span>
  </nav>
</header>

<nav class="mainnav">
  <a href="#" style="left:37px">Home</a>
  <span class="sep" style="left:85px">/</span>
  <a href="#" style="left:110px">Products</a>
  <span class="sep" style="left:174px">/</span>
  <a href="#" style="left:198px">Homes Built</a>
  <span class="sep" style="left:281px">/</span>
  <a href="#" style="left:304px">About</a>
  <span class="sep" style="left:355px">/</span>
  <a href="#" style="left:378px">Contact</a>
  <div class="lang">En
    <svg width="10" height="10" viewBox="0 0 10 10"><circle cx="5" cy="5" r="4.3" fill="none" stroke="#1c1c1c" stroke-width="1.2"/><path d="M1 5 H9 M5 1 Q2.5 5 5 9 M5 1 Q7.5 5 5 9" fill="none" stroke="#1c1c1c" stroke-width=".9"/></svg>
    <svg width="7" height="4" viewBox="0 0 7 4"><path d="M0 0 H7 L3.5 4Z" fill="#1c1c1c"/></svg>
  </div>
  <i class="navrule"></i>
  <a class="social-sm" href="#" style="left:621px" aria-label="Loopa">LP</a>
  <a class="social-sm" href="#" style="left:647px" aria-label="Chirrup">CH</a>
  <a class="social-sm" href="#" style="left:673px" aria-label="Snapfold">SF</a>
</nav>

<section class="hero">
  <svg class="shapes" width="943" height="384" viewBox="0 0 943 384">
    <defs>
      <linearGradient id="wall" x1="0" y1="0" x2="1" y2="1">
        <stop offset="0" stop-color="#3a3a3c"/>
        <stop offset=".45" stop-color="#55524f"/>
        <stop offset="1" stop-color="#2e2d2d"/>
      </linearGradient>
    </defs>
    <polygon points="359,33 943,33 943,384 297,384 451,137" fill="url(#wall)" role="img" aria-label="Photo of a modern home clad in dark steel panels with a glass sliding door"/>
    <polygon points="356,33 415,33 451,137 390,150" fill="#44608e"/>
    <polygon points="390,150 451,137 370,260" fill="#34507e" opacity=".9"/>
    <polygon points="320,300 297,384 385,384" fill="#44608e"/>
  </svg>
  <div class="hero-title">FERN<br>BOLT</div>
  <p class="hero-sub">Aenean eget risusut<br>risus porttitor</p>
  <p class="hero-text">Tulla lobortis neque sit amet enim pharetra, quis consectetur libero lacinia.</p>
  <a class="btn" href="#">SHOP PRODUCTS</a>
  <div class="slider">
    <i class="dot active" style="left:87px"></i>
    <i class="dot" style="left:100px"></i>
    <i class="dot" style="left:112px"></i>
    <i class="dot" style="left:124px"></i>
    <i class="line"></i>
  </div>
</section>

<a class="card" href="#" style="left:124px">
  <div class="photo" role="img" aria-label="Set of black steel pots and pans" style="background:linear-gradient(160deg,#6a6a6c,#2c2c2e 70%,#1a1a1a)"></div>
  <div class="label">STEEL COOKERY <svg width="22" height="6" viewBox="0 0 22 6"><path d="M0 3 H21 M17 0.5 L21 3 L17 5.5" fill="none" stroke="#fff" stroke-width="1"/></svg></div>
</a>
<a class="card" href="#" style="left:359px">
  <div class="photo" role="img" aria-label="Galvanised steel angle brackets" style="background:linear-gradient(160deg,#f4f4f4,#c9cccf 60%,#e8e8e8)"></div>
  <div class="label">BRACKETS <svg width="22" height="6" viewBox="0 0 22 6"><path d="M0 3 H21 M17 0.5 L21 3 L17 5.5" fill="none" stroke="#fff" stroke-width="1"/></svg></div>
</a>
<a class="card" href="#" style="left:595px">
  <div class="photo" role="img" aria-label="Red steel mailbox with white flag outside a house" style="background:linear-gradient(120deg,#8a7a62,#c9403c 55%,#4f6a3a)"></div>
  <div class="label">MAILBOXES <svg width="22" height="6" viewBox="0 0 22 6"><path d="M0 3 H21 M17 0.5 L21 3 L17 5.5" fill="none" stroke="#fff" stroke-width="1"/></svg></div>
</a>

<footer class="footer">
  <div class="f-brand"><span class="mark"></span>FERNBOLT</div>

  <div class="contact" style="top:174px">
    <svg width="11" height="14" viewBox="0 0 11 14"><path d="M5.5 14 C1 8 0.5 6.5 0.5 5.5 A5 5 0 0 1 10.5 5.5 C10.5 6.5 10 8 5.5 14Z" fill="#ff7d0a"/><circle cx="5.5" cy="5.5" r="2" fill="#22304d"/></svg>
    <p>4820 Cobalt Ridge Road<br>Boise ID, USA</p>
  </div>
  <div class="contact" style="top:216px">
    <svg width="12" height="11" viewBox="0 0 12 11"><rect x="0.5" y="2.5" width="11" height="8" fill="none" stroke="#ff7d0a" stroke-width="1.3"/><path d="M0.5 2.5 L6 7 L11.5 2.5" fill="none" stroke="#ff7d0a" stroke-width="1.3"/></svg>
    <p>hello@fernbolt.co<br>We reply within 24 hours</p>
  </div>
  <div class="contact" style="top:260px">
    <svg width="8" height="14" viewBox="0 0 8 14"><path d="M6 1 Q1 2 1 7 Q1 12 6 13" fill="none" stroke="#ff7d0a" stroke-width="2.2"/></svg>
    <p>(208) 0147 552 318<br>Mon-Fri, 9am until 6pm</p>
  </div>

  <div class="col" style="left:309px">
    <h3>INFOMATION</h3>
    <ul><li>About Us</li><li>Contact Us</li><li>FAQs</li><li>Privacy Policy</li><li>Terms &amp; Conditions</li></ul>
  </div>
  <div class="col" style="left:478px;padding-left:32px">
    <h3>HELP</h3>
    <ul><li>FAQs</li><li>Orders and Returns</li><li>Shipping Policies</li><li>International Shipping</li><li>Term &amp; Conditions</li></ul>
  </div>
  <div class="col" style="left:652px;padding-left:32px">
    <h3>YOUR ACCOUNT</h3>
    <ul><li>Cart</li><li>Checkout</li><li>My account</li><li>Contact</li><li>Privacy Policy</li></ul>
  </div>

  <i class="f-rule"></i>
  <p class="copy">© 2020 Fernbolt. All rights reserved.</p>
  <a class="social-lg" href="#" style="left:415px" aria-label="Loopa">LP</a>
  <a class="social-lg" href="#" style="left:454px" aria-label="Chirrup">CH</a>
  <a class="social-lg" href="#" style="left:493px" aria-label="Snapfold">SF</a>

  <span class="pay first" style="left:597px">Paywell</span>
  <span class="pay card-chip" style="left:681px">Cardova</span>
  <span class="pay card-chip" style="left:716px">Vestra</span>
  <span class="pay card-chip" style="left:751px">Amber</span>
  <span class="pay card-chip" style="left:786px">Disko</span>
</footer>

</body>
</html>
```